Talvin Foundation Letterhead

We are a newly established non profit registered in Maryland but operates in Africa, south of the sahara. We offer scholarships to deserving young adults from high school through college. Our color theme for our existing logo is purple, we want a design that is stylish, spellbinding yet a letterhead that projects seriousness. More information on www.thetalvinfoundation.example

Target Market(s)

High school and college students in sub saharan African as well as our donors in the US

Industry/Entity Type

Non Profit

Font styles to use
Script

Requirements
Must have
• Logo at the top and if possible watermark the logo in the middle of the letterhead, contact address,
Should not have
• NA

```html
<!DOCTYPE html>
<html lang="en">
<head>
<meta charset="utf-8">
<title>Talvin Foundation Letterhead</title>
<link href="https://fonts.googleapis.com/css2?family=Cormorant+SC:wght@600&family=Lato:wght@400&display=swap" rel="stylesheet">
<style>
  :root {
    --backdrop: #847b72;
    --paper: #ffffff;
    --purple: #5b2a9a;
    --purple-soft: #8e5cc4;
    --lilac: #ece6f3;
    --ink: #1f1f24;
    --muted: #3d3d45;
  }
  * { box-sizing: border-box; margin: 0; padding: 0; }
  html, body { width: 1200px; height: 795px; overflow: hidden; }
  body {
    background: var(--backdrop);
    font-family: "Lato", "Helvetica Neue", Arial, sans-serif;
    color: var(--ink);
    position: relative;
  }
  .letterhead {
    position: absolute;
    left: 330px; top: 18px;
    width: 540px; height: 760px;
    background: var(--paper);
    box-shadow: 0 6px 18px rgba(0,0,0,.28);
    overflow: hidden;
  }
  .band { position: absolute; left: 0; right: 0; height: 6px; background: var(--purple); }
  .band--top { top: 0; }
  .band--bottom { bottom: 0; }
  .brand {
    position: absolute; top: 40px; left: 0; right: 0;
    display: flex; flex-direction: column; align-items: center; gap: 8px;
  }
  .brand__dot { width: 30px; height: 30px; border-radius: 50%; background: var(--purple); }
  .brand__name {
    font-family: "Cormorant SC", Georgia, serif; font-weight: 600;
    font-size: 17px; letter-spacing: .5px; color: var(--purple);
  }
  .watermark {
    position: absolute; left: 170px; top: 250px;
    width: 200px; height: 200px; border-radius: 50%;
    background: var(--lilac); opacity: .7;
  }
  .letter {
    position: absolute; left: 44px; right: 44px; top: 178px;
    font-size: 9.6px; line-height: 1.45; color: var(--muted);
  }
  .letter__salutation { font-size: 11px; color: var(--ink); margin-bottom: 8px; }
  .letter p + p { margin-top: 12px; }
  .signature {
    position: absolute; left: 46px; top: 520px;
    width: 110px; height: 34px; background: #e9e9ec; border-radius: 3px;
  }
  .swoosh { position: absolute; left: 0; bottom: 6px; width: 540px; height: 34px; }
  .footer {
    position: absolute; right: 36px; bottom: 48px; text-align: right;
  }
  .footer__title { display: flex; align-items: center; justify-content: flex-end; gap: 10px; }
  .footer__rule {
    width: 170px; height: 1.5px;
    background: linear-gradient(90deg, rgba(91,42,154,0), var(--purple));
  }
  .footer__name {
    font-family: "Cormorant SC", Georgia, serif; font-weight: 600;
    font-size: 15px; color: var(--purple); letter-spacing: .4px; white-space: nowrap;
  }
  .footer__address { font-size: 8.6px; color: var(--muted); margin-top: 3px; }
  .footer__contact { font-size: 8.6px; color: var(--muted); margin-top: 2px; white-space: nowrap; }
  .footer__label { color: var(--purple); }
</style>
</head>
<body>
  <main class="letterhead">
    <div class="band band--top"></div>

    <header class="brand">
      <span class="brand__dot"></span>
      <span class="brand__name">Talvin Foundation Inc</span>
    </header>

    <div class="watermark" aria-hidden="true"></div>

    <article class="letter">
      <p class="letter__salutation">Dear Mr. John,</p>
      <p>Lorem Ipsum is simply dummy text of the printing and typesetting industry. Lorem Ipsum has been the industry's standard dummy text ever since the 1500s, when an unknown printer took a galley of type and scrambled it to make a type specimen book. It has survived not only five centuries, but also the leap into electronic typesetting, remaining essentially unchanged.</p>
      <p>The standard chunk of Lorem Ipsum used since the 1500s is reproduced below for those interested. Sections 1.10.32 and 1.10.33 from "de Finibus Bonorum et Malorum" by Cicero are also reproduced in their exact original form, accompanied by English versions from the 1914 translation by H. Rackham.</p>
      <p>Lorem Ipsum is simply dummy text of the printing and typesetting industry. Lorem Ipsum has been the industry's standard dummy text ever since the 1500s, when an unknown printer took a galley of type and scrambled it to make a type specimen book. It has survived not only five centuries, but also the leap into electronic typesetting, remaining essentially unchanged. It was popularised in the</p>
      <p>Lorem Ipsum is simply dummy text of the printing and typesetting industry. Lorem Ipsum has been the industry's standard dummy text ever since the 1500s, when an unknown printer took a galley of type and scrambled it to make a type specimen book. It has survived not only five centuries, but also the leap into electronic typesetting, remaining essentially unchanged. It was popularised in the</p>
    </article>

    <div class="signature" role="img" aria-label="Handwritten signature"></div>

    <footer class="footer">
      <div class="footer__title">
        <span class="footer__rule" aria-hidden="true"></span>
        <span class="footer__name">The Talvin Foundation Inc</span>
      </div>
      <div class="footer__address">12 Willow Brook Lane, Suite 3, Fairview, Md 20910</div>
      <div class="footer__contact"><span class="footer__label">email:</span> admin@thetalvinfoundation.example <span class="footer__label">website:</span> www.thetalvinfoundation.example</div>
    </footer>

    <svg class="swoosh" viewBox="0 0 540 34" aria-hidden="true">
      <defs>
        <linearGradient id="swoosh-fill" x1="0" x2="1">
          <stop offset="0" stop-color="#5b2a9a" stop-opacity="0"/>
          <stop offset=".5" stop-color="#5b2a9a"/>
          <stop offset="1" stop-color="#8e5cc4"/>
        </linearGradient>
      </defs>
      <path d="M120 32 Q330 22 540 6" fill="none" stroke="url(#swoosh-fill)" stroke-width="1.6"/>
    </svg>

    <div class="band band--bottom"></div>
  </main>
</body>
</html>
```